Harborline Flood Protection, Inc

I need the following
Logo
Truck wrap
We are a new flood protection company for residential homes and commercial businesses in Florida that is designed to keep flood waters from entering entry points
It is a rubber gasketed aluminum barrier system with permanent brackets installed to masonry structures.
We want to consider including a photo of an installation on our vehicles.
We would like the font to be legible from a distance yet have the tailgates be read easily at a traffic light. We are open to color selection but we want to differentiate from others.
No super hero stuff, no gimmicky nonsense - just super clean and not busy. Need to be memorable. Less is more.
Can show flooding but NO WAVES

See attached photos of similar installations

```html
<!DOCTYPE html>
<html lang="en">
<head>
<meta charset="utf-8">
<title>Harborline Flood Protection, Inc — Truck Wrap</title>
<link href="https://fonts.googleapis.com/css2?family=Montserrat:ital,wght@0,400;0,600;0,700;1,700;1,800&display=swap" rel="stylesheet">
<style>
  :root {
    --bg: #eef0f3;
    --navy: #173e66;
    --blue: #1f88c4;
    --sky: #3ba3d9;
    --white: #ffffff;
    --ink: #1b1d22;
    --edge: #c9ced6;
    --photo-a: #6f93a8;
    --photo-b: #b9c0c4;
  }
  html, body {
    margin: 0;
    padding: 0;
    width: 1200px;
    height: 3625px;
    overflow: hidden;
    background: var(--bg);
    font-family: "Montserrat", Arial, sans-serif;
  }
  .canvas { position: relative; width: 1200px; height: 3625px; }
  .panel {
    position: absolute;
    background: var(--white);
    border: 4px solid var(--edge);
    overflow: hidden;
    box-sizing: border-box;
  }
  .panel svg.art { position: absolute; inset: 0; width: 100%; height: 100%; }
  .brand {
    position: absolute;
    display: flex;
    align-items: center;
    gap: 22px;
  }
  .brand-dot {
    flex: none;
    border-radius: 50%;
    background: var(--navy);
  }
  .brand-name {
    font-weight: 700;
    color: var(--ink);
    line-height: 1.05;
    letter-spacing: 0.2px;
  }
  .tagline {
    position: absolute;
    color: var(--sky);
    font-weight: 400;
    text-align: center;
  }
  .phone {
    position: absolute;
    display: flex;
    align-items: center;
    gap: 12px;
    color: var(--white);
    font-weight: 800;
    font-style: italic;
    letter-spacing: 1px;
  }
  .phone svg { flex: none; }

  /* front header */
  .front { left: 320px; top: 260px; width: 560px; height: 210px; }
  .front .brand { left: 40px; top: 48px; }
  .front .brand-dot { width: 96px; height: 96px; }
  .front .brand-name { font-size: 40px; }

  /* right side */
  .side-right { left: 80px; top: 1230px; width: 1040px; height: 380px; }
  .side-right .brand { left: 330px; top: 62px; }
  .side-right .brand-dot { width: 100px; height: 100px; }
  .side-right .brand-name { font-size: 50px; }
  .side-right .tagline { left: 420px; width: 380px; top: 218px; font-size: 30px; }
  .side-right .phone { left: 410px; top: 272px; font-size: 42px; }

  /* rear */
  .rear { left: 300px; top: 2020px; width: 600px; height: 560px; }
  .rear .brand { left: 50px; top: 70px; }
  .rear .brand-dot { width: 80px; height: 80px; }
  .rear .brand-name { font-size: 36px; }
  .rear .tagline { left: 0; width: 600px; top: 210px; font-size: 30px; }
  .rear .phone { left: 112px; top: 350px; font-size: 36px; }

  /* left side */
  .side-left { left: 80px; top: 2960px; width: 1040px; height: 380px; }
  .side-left .brand { left: 40px; top: 62px; }
  .side-left .brand-dot { width: 100px; height: 100px; }
  .side-left .brand-name { font-size: 50px; }
  .side-left .tagline { left: 120px; width: 380px; top: 218px; font-size: 30px; }
  .side-left .phone { left: 110px; top: 272px; font-size: 42px; }
</style>
</head>
<body>
<div class="canvas">

  <!-- Front header -->
  <section class="panel front">
    <div class="brand">
      <span class="brand-dot"></span>
      <span class="brand-name">Harborline Flood<br>Protection, Inc</span>
    </div>
  </section>

  <!-- Right side -->
  <section class="panel side-right">
    <svg class="art" viewBox="0 0 1040 380" preserveAspectRatio="none">
      <rect width="1040" height="380" fill="var(--navy)"/>
      <path d="M250 0 L1040 0 L1040 242 C900 207 700 202 520 227 C400 244 300 252 266 182 C233 112 230 50 250 0 Z" fill="var(--blue)"/>
      <path d="M272 0 L1040 0 L1040 220 C900 185 700 180 520 205 C420 220 320 228 290 170 C258 110 254 50 272 0 Z" fill="var(--white)"/>
      <circle cx="150" cy="128" r="84" fill="var(--sky)"/>
      <circle cx="150" cy="128" r="78" fill="var(--photo-a)" role="img" aria-label="Photo of a home with a pool protected by flood barriers"/>
      <circle cx="250" cy="282" r="74" fill="var(--sky)"/>
      <circle cx="250" cy="282" r="68" fill="var(--photo-b)" role="img" aria-label="Photo of an aluminum flood barrier installed at a doorway"/>
    </svg>
    <div class="brand">
      <span class="brand-dot"></span>
      <span class="brand-name">Harborline Flood<br>Protection, Inc</span>
    </div>
    <div class="tagline">Peace of Mind</div>
    <div class="phone">
      <svg width="36" height="36" viewBox="0 0 24 24" fill="none" stroke="var(--white)" stroke-width="2" stroke-linecap="round" stroke-linejoin="round"><path d="M22 16.9v3a2 2 0 0 1-2.2 2 19.8 19.8 0 0 1-8.6-3.1 19.5 19.5 0 0 1-6-6A19.8 19.8 0 0 1 2.1 4.2 2 2 0 0 1 4.1 2h3a2 2 0 0 1 2 1.7c.1.9.4 1.8.7 2.7a2 2 0 0 1-.5 2.1L8 9.8a16 16 0 0 0 6 6l1.3-1.3a2 2 0 0 1 2.1-.5c.9.3 1.8.6 2.7.7a2 2 0 0 1 1.9 2.2z"/><path d="M15 5a5 5 0 0 1 4 4M15 1a9 9 0 0 1 8 8"/></svg>
      <span>0198-765-432</span>
    </div>
  </section>

  <!-- Rear -->
  <section class="panel rear">
    <svg class="art" viewBox="0 0 600 560" preserveAspectRatio="none">
      <rect width="600" height="560" fill="var(--navy)"/>
      <path d="M0 0 H600 V140 C590 280 480 318 300 318 C120 318 10 280 0 140 Z" fill="var(--blue)"/>
      <path d="M0 0 H600 V120 C588 262 478 300 300 300 C122 300 12 262 0 120 Z" fill="var(--white)"/>
    </svg>
    <div class="brand">
      <span class="brand-dot"></span>
      <span class="brand-name">Harborline Flood<br>Protection, Inc</span>
    </div>
    <div class="tagline">Peace of Mind</div>
    <div class="phone">
      <svg width="30" height="30" viewBox="0 0 24 24" fill="none" stroke="var(--white)" stroke-width="2" stroke-linecap="round" stroke-linejoin="round"><path d="M22 16.9v3a2 2 0 0 1-2.2 2 19.8 19.8 0 0 1-8.6-3.1 19.5 19.5 0 0 1-6-6A19.8 19.8 0 0 1 2.1 4.2 2 2 0 0 1 4.1 2h3a2 2 0 0 1 2 1.7c.1.9.4 1.8.7 2.7a2 2 0 0 1-.5 2.1L8 9.8a16 16 0 0 0 6 6l1.3-1.3a2 2 0 0 1 2.1-.5c.9.3 1.8.6 2.7.7a2 2 0 0 1 1.9 2.2z"/><path d="M15 5a5 5 0 0 1 4 4M15 1a9 9 0 0 1 8 8"/></svg>
      <span>0198-765-432</span>
    </div>
  </section>

  <!-- Left side -->
  <section class="panel side-left">
    <svg class="art" viewBox="0 0 1040 380" preserveAspectRatio="none">
      <g transform="translate(1040 0) scale(-1 1)">
        <rect width="1040" height="380" fill="var(--navy)"/>
        <path d="M250 0 L1040 0 L1040 242 C900 207 700 202 520 227 C400 244 300 252 266 182 C233 112 230 50 250 0 Z" fill="var(--blue)"/>
        <path d="M272 0 L1040 0 L1040 220 C900 185 700 180 520 205 C420 220 320 228 290 170 C258 110 254 50 272 0 Z" fill="var(--white)"/>
        <circle cx="150" cy="128" r="84" fill="var(--sky)"/>
        <circle cx="150" cy="128" r="78" fill="var(--photo-a)" role="img" aria-label="Photo of a home with a pool protected by flood barriers"/>
        <circle cx="250" cy="282" r="74" fill="var(--sky)"/>
        <circle cx="250" cy="282" r="68" fill="var(--photo-b)" role="img" aria-label="Photo of an aluminum flood barrier installed at a doorway"/>
      </g>
    </svg>
    <div class="brand">
      <span class="brand-dot"></span>
      <span class="brand-name">Harborline Flood<br>Protection, Inc</span>
    </div>
    <div class="tagline">Peace of Mind</div>
    <div class="phone">
      <svg width="36" height="36" viewBox="0 0 24 24" fill="none" stroke="var(--white)" stroke-width="2" stroke-linecap="round" stroke-linejoin="round"><path d="M22 16.9v3a2 2 0 0 1-2.2 2 19.8 19.8 0 0 1-8.6-3.1 19.5 19.5 0 0 1-6-6A19.8 19.8 0 0 1 2.1 4.2 2 2 0 0 1 4.1 2h3a2 2 0 0 1 2 1.7c.1.9.4 1.8.7 2.7a2 2 0 0 1-.5 2.1L8 9.8a16 16 0 0 0 6 6l1.3-1.3a2 2 0 0 1 2.1-.5c.9.3 1.8.6 2.7.7a2 2 0 0 1 1.9 2.2z"/><path d="M15 5a5 5 0 0 1 4 4M15 1a9 9 0 0 1 8 8"/></svg>
      <span>0198-765-432</span>
    </div>
  </section>

</div>
</body>
</html>
```